The amber lantern with an elephant incorporated in the background

Target Market(s)

Real estate

Industry/Entity Type

Real Estate

Contact Information for Business Card

On back on want my name & number
In front I want the business name, "the amber lantern", below to say staging & design

Logo Text

The amber lantern

Font styles to use
Serif

Colors
000000

Requirements
Must have
• I want an elephant behind the writing in gold transperant

```html
<!DOCTYPE html>
<html lang="en">
<head>
<meta charset="UTF-8">
<title>The Amber Lantern – Business Cards</title>
<link rel="stylesheet" href="https://fonts.googleapis.com/css2?family=Cormorant+Garamond:wght@400;500;700&display=swap">
<style>
  :root {
    --stage: #1b1b1b;
    --card: #232323;
    --gold: #c2a052;
    --gold-deep: #a8843a;
    --gold-light: #e6c978;
    --ghost: #3d3a30;
    --white: #f4f4f4;
  }
  * { margin: 0; padding: 0; box-sizing: border-box; }
  html, body {
    width: 1200px; height: 1000px; overflow: hidden;
    background: var(--stage);
    font-family: "Cormorant Garamond", Georgia, serif;
  }
  .card {
    position: absolute;
    left: 215px;
    width: 770px; height: 440px;
    background: var(--card);
    box-shadow: 0 10px 30px rgba(0,0,0,0.5);
    overflow: hidden;
  }
  .card--front { top: 40px; }
  .card--back { top: 520px; }

  .front__elephant {
    position: absolute;
    left: 215px; top: 0;
    width: 340px; height: 440px;
    background: radial-gradient(ellipse at 50% 35%, var(--ghost) 0%, rgba(61,58,48,0.6) 55%, rgba(35,35,35,0) 80%);
  }
  .front__logo {
    position: absolute;
    left: 190px; top: 150px;
    width: 390px; height: 84px;
    border: 2px solid var(--white);
    display: flex; align-items: center; justify-content: center;
    color: var(--white);
    font-size: 22px; font-weight: 500;
    letter-spacing: 0.3em;
    text-transform: uppercase;
    white-space: nowrap;
  }
  .front__tagline {
    position: absolute;
    left: 190px; top: 250px;
    width: 390px;
    text-align: center;
    color: var(--gold);
    font-size: 16px; font-weight: 500;
    letter-spacing: 0.35em;
    text-transform: uppercase;
  }

  .back__title {
    position: absolute;
    left: 50px; top: 50px;
    color: var(--gold);
    font-size: 36px; font-weight: 700;
    letter-spacing: 0.06em;
    text-transform: uppercase;
    white-space: nowrap;
  }
  .back__contact {
    position: absolute;
    left: 58px; top: 318px;
    padding-left: 12px;
    border-left: 3px solid var(--gold);
  }
  .back__name {
    color: var(--gold);
    font-size: 34px; font-weight: 700;
    letter-spacing: 0.04em;
    line-height: 1.1;
    text-transform: uppercase;
    white-space: nowrap;
  }
  .back__phone {
    color: var(--white);
    font-size: 19px; font-weight: 500;
    margin-top: 4px;
  }
  .back__elephant {
    position: absolute;
    left: 555px; top: 290px;
    width: 190px; height: 135px;
    border-radius: 45% 50% 30% 30%;
    background: linear-gradient(135deg, var(--gold-light), var(--gold-deep));
  }
</style>
</head>
<body>
  <section class="card card--front">
    <div class="front__elephant" role="img" aria-label="Faint gold elephant head seen from the front, behind the name"></div>
    <div class="front__logo">The Amber Lantern</div>
    <p class="front__tagline">Staging &amp; Design</p>
  </section>

  <section class="card card--back">
    <h1 class="back__title">The Amber Lantern</h1>
    <div class="back__contact">
      <p class="back__name">Daniel Moreau</p>
      <p class="back__phone">+000 987 654 321</p>
    </div>
    <div class="back__elephant" role="img" aria-label="Gold elephant figurine with raised trunk"></div>
  </section>
</body>
</html>
```